Etiketten für Obsthof in Friedrichshafen am Bodensee
Zielgruppe
Wir sind ein Obsthof in Friedrichshafen am Bodensee und verkaufen in unserem Hofladen unsere selbsthergestellten Produkte. Dabei zeichnet uns besonders aus, dass wir unsere Produkte aus eigens angebautem Obst Herstellen wie zum Beispiel Marmeladen, Säfte, Sirup, Schnaps oder Liköre.
Unsere Zielgruppe sind Kundinnen und Kunden, die Wert auf Regionalität, Transparenz bei der Produktherstellung und Qualität der Inhaltsstoffe legen.
Aufgabenstellung
Uns ist besonders wichtig, dass die Etiketten widerspiegeln, dass die Produkte selbst hergestellt wurden und hochwertig sind.
Die Etiketten sollten alle auf einander abgestimmt sein, sodass sie sich wie eine klare Linie durch das ganze Sortiment ziehen. Dementsprechend soll ein universelles Etikett erstellt werden, das wir für alle unsere Produkte verwenden können. Hierbei ist es wichtig, dass wir im Nachhinein selbst die Produktbeschreibung auf dem Etikett an das jeweilige Produkt anpassen können.
Es sollte auch Platz sein für die Inhaltsstoffe, unsere Anschrift, Mindesthaltbarkeitsdatum und die Inhaltsmenge.
https://www.wendrahof-polmit.com/hofladen-und-produkte.htm
in diese Richtung könnte ich mir die Ausführung vorstellen.

```html
<!DOCTYPE html>
<html lang="de">
<head>
<meta charset="utf-8">
<title>Kernau Obsthof – Etiketten</title>
<link rel="stylesheet" href="https://fonts.googleapis.com/css2?family=Patrick+Hand&display=swap">
<style>
  :root {
    --canvas: #f2f2f2;
    --label: #ffffff;
    --ink: #4a4a4a;
    --ink-soft: #8a8a8a;
    --dash: #9a9a9a;
    --copper: #b8714e;
    --copper-light: #efcdb9;
    --copper-pale: #f8e6dc;
  }
  * { box-sizing: border-box; margin: 0; padding: 0; }
  html, body { width: 1200px; height: 849px; overflow: hidden; }
  body {
    background: var(--canvas);
    font-family: "Patrick Hand", "Comic Sans MS", cursive;
    position: relative;
  }
  .label {
    position: absolute;
    background: var(--label);
    border-radius: 16px;
    overflow: hidden;
    box-shadow: 0 2px 8px rgba(0,0,0,0.06);
  }
  .label--sirup   { left: 140px; top: 522px; width: 188px; height: 220px; }
  .label--likoer  { left: 536px; top: 475px; width: 176px; height: 243px; }
  .label--konfi   { left: 918px; top: 530px; width: 189px; height: 221px; }

  .foliage {
    position: absolute;
    pointer-events: none;
  }
  .foliage--top {
    right: 0; top: 0; width: 40px; height: 58%;
    background: linear-gradient(160deg, var(--copper-light) 0%, var(--copper-pale) 55%, rgba(248,230,220,0) 100%);
    border-top-right-radius: 16px;
  }
  .foliage--bottom {
    left: 0; bottom: 0; width: 56px; height: 52%;
    background: linear-gradient(20deg, var(--copper) 0%, var(--copper-light) 45%, rgba(248,230,220,0) 100%);
    border-bottom-left-radius: 16px;
  }

  .frame {
    position: absolute;
    left: 9px; right: 15px; top: 22px; bottom: 20px;
    border: 1.3px dashed var(--dash);
    border-radius: 3px;
  }

  .brand {
    position: absolute;
    top: 10px; left: 0; right: 0;
    display: flex; align-items: center; justify-content: center; gap: 6px;
  }
  .brand__dot {
    width: 20px; height: 20px; border-radius: 50%;
    background: var(--copper);
  }
  .brand__name {
    font-size: 19px; line-height: 1; color: var(--copper);
    background: var(--label); padding: 2px 4px;
  }

  .tagline {
    position: absolute;
    left: 0; right: 0; top: 60px;
    width: 100%; height: 30px;
  }
  .tagline text {
    font-family: "Patrick Hand", "Comic Sans MS", cursive;
    font-size: 7.5px; letter-spacing: 0.6px; fill: var(--ink-soft);
  }

  .product {
    position: absolute; left: 0; right: 0; top: 88px;
    text-align: center; color: var(--ink);
    font-size: 33px; line-height: 0.92;
  }
  .label--likoer .product { top: 92px; }

  .volume {
    position: absolute;
    bottom: 13px; left: 50%; transform: translateX(-45%);
    background: var(--label); padding: 0 4px;
    font-size: 13px; line-height: 1; color: var(--ink-soft);
  }
</style>
</head>
<body>

  <article class="label label--sirup">
    <div class="foliage foliage--top" role="img" aria-label="Kupferfarbene Blätterranke, oben rechts"></div>
    <div class="foliage foliage--bottom" role="img" aria-label="Kupferfarbene Blätterranke, unten links"></div>
    <div class="frame"></div>
    <div class="brand"><span class="brand__dot"></span><span class="brand__name">Kernau Obsthof</span></div>
    <svg class="tagline" viewBox="0 0 188 30" aria-hidden="true">
      <path id="arc-sirup" d="M44 26 Q94 4 144 26" fill="none"/>
      <text><textPath href="#arc-sirup" startOffset="50%" text-anchor="middle">100% aus eigenem Anbau</textPath></text>
    </svg>
    <h2 class="product">Holunder<br>Sirup</h2>
    <p class="volume">500 ml ℮</p>
  </article>

  <article class="label label--likoer">
    <div class="foliage foliage--top" role="img" aria-label="Kupferfarbene Blätterranke, oben rechts"></div>
    <div class="foliage foliage--bottom" role="img" aria-label="Kupferfarbene Blätterranke, unten links"></div>
    <div class="frame"></div>
    <div class="brand"><span class="brand__dot"></span><span class="brand__name">Kernau Obsthof</span></div>
    <svg class="tagline" viewBox="0 0 176 30" aria-hidden="true">
      <path id="arc-likoer" d="M38 26 Q88 4 138 26" fill="none"/>
      <text><textPath href="#arc-likoer" startOffset="50%" text-anchor="middle">100% aus eigenem Anbau</textPath></text>
    </svg>
    <h2 class="product">Walnuss<br>Likör</h2>
    <p class="volume">500 ml ℮</p>
  </article>

  <article class="label label--konfi">
    <div class="foliage foliage--top" role="img" aria-label="Kupferfarbene Blätterranke, oben rechts"></div>
    <div class="foliage foliage--bottom" role="img" aria-label="Kupferfarbene Blätterranke, unten links"></div>
    <div class="frame"></div>
    <div class="brand"><span class="brand__dot"></span><span class="brand__name">Kernau Obsthof</span></div>
    <svg class="tagline" viewBox="0 0 189 30" aria-hidden="true">
      <path id="arc-konfi" d="M44 26 Q94 4 144 26" fill="none"/>
      <text><textPath href="#arc-konfi" startOffset="50%" text-anchor="middle">100% aus eigenem Anbau</textPath></text>
    </svg>
    <h2 class="product">Sauerkirsch<br>Konfitüre</h2>
    <p class="volume">350 ml</p>
  </article>

</body>
</html>
```